Business Card Design Project

I require a business card with the following information on them for various different people;
name
m:
f:
e:
I have a logo already and will attached that. We are in the construction industry. I require something clean and simple but eye catching at the same time. You can use another colour with our logo if you like and you can style the logo as well if you wish. I am open.
Also it needs to be front and back design.
Industry/Entity Type
Construction
Requirements
Must have
- Logo, name, mobile, fax and email address.
Front and back design

```html
<!DOCTYPE html>
<html lang="en">
<head>
<meta charset="utf-8">
<title>Stonebridge Developments – Business Cards</title>
<link rel="stylesheet" href="https://fonts.googleapis.com/css2?family=Questrial&family=Open+Sans:wght@400;600&display=swap">
<style>
  :root {
    --bg: #d9d9d7;
    --card: #ffffff;
    --green: #4cb52f;
    --ink: #3a3a3a;
    --grey: #5c5c5c;
    --dark-band: #2b2622;
  }
  * { margin: 0; padding: 0; box-sizing: border-box; }
  html, body { width: 1200px; height: 944px; overflow: hidden; }
  body {
    background: var(--bg);
    position: relative;
    font-family: "Questrial", "Century Gothic", sans-serif;
    color: var(--ink);
  }
  .card {
    position: absolute;
    width: 620px;
    height: 354px;
    background: var(--card);
    border-radius: 24px;
    box-shadow: 0 10px 28px rgba(0,0,0,0.22);
    overflow: hidden;
  }
  .card--back { left: 70px; top: 80px; }
  .card--front { left: 510px; top: 500px; }

  .brand {
    display: flex;
    align-items: center;
    gap: 14px;
  }
  .brand__mark {
    width: 34px; height: 34px;
    background: var(--green);
    flex: none;
  }
  .brand__name {
    font-size: 38px;
    color: var(--grey);
    letter-spacing: 0.5px;
    white-space: nowrap;
  }
  .card--back .brand {
    position: absolute;
    left: 0; right: 0; top: 118px;
    justify-content: center;
  }
  .card--back .website {
    position: absolute;
    left: 0; right: 0; top: 222px;
    text-align: center;
    font-family: "Open Sans", Arial, sans-serif;
    font-size: 19px;
    letter-spacing: 1px;
    color: var(--ink);
  }

  .card__panel { position: absolute; inset: 0; }
  .card--front .brand {
    position: absolute; left: 46px; top: 66px;
    gap: 12px;
  }
  .card--front .brand__mark { width: 24px; height: 24px; }
  .card--front .brand__name { font-size: 26px; letter-spacing: 0.3px; }

  .contacts {
    position: absolute; left: 46px; top: 190px;
    list-style: none;
    font-family: "Open Sans", Arial, sans-serif;
    font-size: 17px;
    line-height: 25px;
    color: var(--ink);
  }
  .contacts li { display: flex; align-items: center; gap: 10px; }
  .contacts svg { width: 14px; height: 14px; flex: none; }
  .contacts .accent { color: var(--green); }

  .person {
    position: absolute; right: 40px; bottom: 40px;
    text-align: right;
    font-family: "Open Sans", Arial, sans-serif;
    color: #ffffff;
  }
  .person__name { font-size: 23px; font-weight: 400; }
  .person__role { font-size: 16px; margin-top: 2px; }
</style>
</head>
<body>

<section class="card card--back" aria-label="Card back">
  <div class="brand">
    <span class="brand__mark"></span>
    <span class="brand__name">Stonebridge Developments</span>
  </div>
  <p class="website">www.stonebridgebuild.com</p>
</section>

<section class="card card--front" aria-label="Card front">
  <svg class="card__panel" viewBox="0 0 620 354" preserveAspectRatio="none" aria-hidden="true">
    <defs>
      <linearGradient id="panelGreen" x1="0" y1="0" x2="1" y2="1">
        <stop offset="0" stop-color="#6cc644"/>
        <stop offset="1" stop-color="#3fa82a"/>
      </linearGradient>
    </defs>
    <path d="M476 0 Q452 220 306 354 L620 354 L620 0 Z" fill="var(--dark-band)"/>
    <path d="M492 0 Q470 220 336 354 L620 354 L620 0 Z" fill="url(#panelGreen)"/>
  </svg>

  <div class="brand">
    <span class="brand__mark"></span>
    <span class="brand__name">Stonebridge Developments</span>
  </div>

  <ul class="contacts">
    <li>
      <svg viewBox="0 0 14 14"><path d="M3 1 L5.5 1 L6.5 4 L5 5.2 Q6.3 8 8.8 9 L10 7.5 L13 8.5 L13 11 Q12 13 9.5 12.5 Q2.5 10.5 1.5 3.5 Q1.5 1.5 3 1Z" fill="var(--green)"/></svg>
      <span>512-555-0140</span>
    </li>
    <li>
      <svg viewBox="0 0 14 14"><rect x="3.5" y="1" width="7" height="4" fill="none" stroke="var(--green)" stroke-width="1.4"/><rect x="1" y="5" width="12" height="6" rx="1" fill="var(--green)"/><rect x="3.5" y="9" width="7" height="4" fill="#fff" stroke="var(--green)" stroke-width="1.4"/></svg>
      <span>512-555-0141</span>
    </li>
    <li>
      <svg viewBox="0 0 14 14"><rect x="1" y="3" width="12" height="8.5" rx="1" fill="var(--green)"/><path d="M1.5 3.5 L7 8 L12.5 3.5" fill="none" stroke="#fff" stroke-width="1.2"/></svg>
      <span>info@stonebridgebuild.com</span>
    </li>
    <li>
      <svg viewBox="0 0 14 14"><circle cx="7" cy="7" r="6" fill="var(--green)"/></svg>
      <span>www.<span class="accent">stonebridgebuild</span>.com</span>
    </li>
  </ul>

  <div class="person">
    <p class="person__name">Marcus Whitfield</p>
    <p class="person__role">director</p>
  </div>
</section>

</body>
</html>
```